依頼詳細
完成見学会を開催するにあたり、来場者の集客のためのチラシの制作をお願いしたいです。コピーと素材はこちらで準備します。
誌面のデザイン、マップの描きおこし、図面のトレースをお願いします。
今回、完成写真はありませんのでイメージ写真を組み合わせたデザインでお願いします(参考資料①)
裏面は、設計士の顔写真とコメント、お施主様のコメントを入れてください。それと会社データ以外のスペースにどのような情報を入れたらいいかの提案はお願いできますか。

誌面デザインは参考資料①のようにイメージ写真の組み合わせで、写真の色味も資料のようにお願いします。
若い層(新築世代)へのアピールもしていきたいため、ポップよりも重厚感、でも古くさくなくモダンテイストを意識していただきたいです。

以上はこちらの要望ですが、デザイナーさんの個性を生かした自由な発想のデザインもお待ちしています。「グラフィカル」な誌面を希望します。
記載項目
表面:タイトル、キャッチコピー、ボディコピー、開催日時、場所
裏面:設計/p.u.t.design 施工/株式会社森川栄三商店
問い合わせ番号、HPアドレス、QRコード、営業時間などの会社概要 ※会社のロゴ入り
サイズ
A4
ページ数
両面
希望イメージ
シンプル 複雑
単色 カラフル
暗い 明るい
日常 高級
遊び心 厳粛
未来的 伝統的
女性的 男性的
希望する色
納品ファイル
• イラストレーター形式 (.ai)
補足説明
タイトル、キャッチコピー、ボディコピーはダミーでお願いします。
ロゴも送ります。
イメージ写真はこちらで購入して、正式に発注が決まってからお送りします。
提案段階ではダミー写真でお願いします。
設計士の顔写真、コメントもダミーで大丈夫です。
マップと図面のトレースは正式に発注後に作成、提案段階ではダミーで大丈夫です。

表面の背景に古民家を想像させる木の写真を使用していたところ

細かい修正にも、即座に対応していただきまして、ありがとうございました。

```html
<!DOCTYPE html>
<html lang="ja">
<head>
<meta charset="utf-8">
<title>古民家リノベーション完成見学会</title>
<link href="https://fonts.googleapis.com/css2?family=Shippori+Mincho:wght@500;700;800&family=Cormorant+Garamond:wght@500;600&family=Noto+Sans+JP:wght@400;500&display=swap" rel="stylesheet">
<style>
  :root {
    --plum: #34232f;
    --paper: #ffffff;
    --ink: #241a1f;
    --mist: #d3cacd;
    --map: #ecebe8;
  }
  * { box-sizing: border-box; margin: 0; padding: 0; }
  html, body { width: 885px; height: 1200px; overflow: hidden; background: var(--paper); }
  .flyer { position: relative; width: 885px; height: 1200px; background: var(--paper); font-family: "Shippori Mincho", serif; color: var(--ink); }

  .header { position: absolute; left: 0; top: 0; width: 885px; height: 488px; background: var(--plum); }

  .brand { position: absolute; left: 34px; top: 26px; color: var(--paper); }
  .brand-name { display: flex; align-items: center; gap: 10px; font-size: 22px; font-weight: 700; letter-spacing: 0.08em; }
  .brand-mark { width: 26px; height: 26px; background: var(--paper); }
  .brand-partner { margin-top: 14px; padding-top: 10px; border-top: 1px solid var(--mist); width: 240px; font-family: "Cormorant Garamond", serif; font-size: 20px; letter-spacing: 0.04em; }

  .catch { position: absolute; left: 508px; top: 22px; color: var(--paper); font-size: 36px; font-weight: 700; line-height: 1.26; letter-spacing: 0.06em; }

  .header-photo { position: absolute; left: 455px; top: 176px; width: 282px; height: 192px; background: linear-gradient(135deg, #e9e4dc 0%, #b7a28a 45%, #4b3a2c 100%); }

  .body-copy { position: absolute; left: 530px; top: 382px; width: 335px; color: var(--paper); font-family: "Noto Sans JP", sans-serif; font-size: 12.5px; line-height: 1.75; }

  .open-house { position: absolute; left: 34px; top: 162px; color: var(--mist); font-family: "Cormorant Garamond", serif; font-weight: 500; font-size: 62px; line-height: 1; letter-spacing: 0.03em; }
  .open-lead { position: absolute; left: 34px; top: 284px; color: var(--paper); font-size: 24px; font-weight: 500; line-height: 1.5; letter-spacing: 0.04em; }

  .photo { position: absolute; }
  .photo-dining { left: 15px; top: 496px; width: 396px; height: 304px; background: linear-gradient(160deg, #d9cbb7 0%, #8c6c50 55%, #3a2a1f 100%); }
  .photo-dining .initial { position: absolute; left: 18px; top: 6px; color: rgba(255,255,255,0.82); font-family: "Cormorant Garamond", serif; font-size: 150px; font-weight: 500; line-height: 1; }
  .photo-resident { left: 416px; top: 496px; width: 170px; height: 274px; background: linear-gradient(180deg, #e6dfd3 0%, #b59d83 60%, #6d5643 100%); }
  .photo-room { left: 591px; top: 496px; width: 279px; height: 288px; background: linear-gradient(200deg, #f2ece2 0%, #b49474 50%, #4e3929 100%); }
  .photo-hearth { left: 15px; top: 805px; width: 396px; height: 380px; background: linear-gradient(180deg, #2c211b 0%, #5a4332 50%, #8d7058 100%); }
  .photo-corridor { left: 735px; top: 789px; width: 135px; height: 396px; background: linear-gradient(180deg, #d8c8b1 0%, #7c5b41 55%, #35261c 100%); }

  .title-box { position: absolute; left: 416px; top: 775px; width: 314px; height: 210px; background: var(--paper); padding: 18px 0 0 22px; }
  .title { font-weight: 800; line-height: 1.18; letter-spacing: 0.02em; }
  .title .l1 { display: block; font-size: 60px; }
  .title .l2 { display: block; font-size: 41px; }
  .title .l3 { display: block; font-size: 55px; }

  .date { position: absolute; left: 436px; top: 992px; font-weight: 700; font-size: 44px; line-height: 1; letter-spacing: 0.01em; }
  .date small { font-size: 16px; letter-spacing: 0.04em; }
  .time { position: absolute; left: 520px; top: 1044px; font-family: "Noto Sans JP", sans-serif; font-size: 12px; line-height: 1.2; letter-spacing: 0.06em; }

  .map { position: absolute; left: 436px; top: 1066px; width: 280px; height: 92px; background: var(--map); }
  .venue { position: absolute; left: 436px; top: 1164px; font-family: "Noto Sans JP", sans-serif; font-size: 11px; line-height: 1.3; }
</style>
</head>
<body>
<main class="flyer">
  <header class="header">
    <div class="brand">
      <div class="brand-name"><span class="brand-mark"></span>森川栄三商店</div>
      <div class="brand-partner">p.u.t.design</div>
    </div>
    <h2 class="catch">古いのに新しい。<br>新しいのに<br>懐かしい。</h2>
    <div class="header-photo" role="img" aria-label="障子と木の梁が残る古民家の和室の写真"></div>
    <p class="body-copy">古民家再生工事では、古くて良い柱や梁を残したまま、建物の構造補強・断熱・採光を考えて、現代の暮らしに合った住まいを造っています。</p>
    <p class="open-house">OPEN<br>HOUSE</p>
    <p class="open-lead">癒しとくつろぎの空間<br>をご提案いたします。</p>
  </header>

  <div class="photo photo-dining" role="img" aria-label="木のテーブルと椅子が並ぶ明るいダイニングの写真"><span class="initial">R</span></div>
  <div class="photo photo-resident" role="img" aria-label="古民家の室内に佇む住まい手の写真"></div>
  <div class="photo photo-room" role="img" aria-label="ペンダント照明とダイニングセットのある室内の写真"></div>
  <div class="photo photo-hearth" role="img" aria-label="黒い梁と囲炉裏のある土間の写真"></div>
  <div class="photo photo-corridor" role="img" aria-label="木の床と建具が続く廊下の写真"></div>

  <section class="title-box">
    <h1 class="title"><span class="l1">古民家</span><span class="l2">リノベーション</span><span class="l3">完成見学会</span></h1>
  </section>

  <p class="date">7/7<small>SAT</small>・8<small>SUN</small></p>
  <p class="time">AM 10:00 〜 PM 4:00</p>
  <div class="map" role="img" aria-label="会場までの道順を示す地図"></div>
  <p class="venue">会場</p>
</main>
</body>
</html>
```